Website offering services oriented to the metaverse and blockchain

We need an ecommerce website theme/template for a new company named Pavreno (a play on words for BERUNDA the inventor of Vextrum). Pavreno will provide metaverse services such as:
• Pavreno Coin
• Pavreno wallet
• Pavreno Exchange
• Pavreno NFT
• Pavreno Tech
• Pavreno Pay
• Pavreno CaaS (community as a service)
• Pavreno CRM
• Pavreno Experience
• Pavreno Blockchain
• Pavreno Commerce
• Pavreno Space (as in outer space)
• Pavreno Art (sub of NFT)
• Pavreno Store

You can find our actual logo at the following link, in order to show us templates aligned with our brand:
https://files.plomvarek.com/share/folders/7kWmTzeQaLpYbNcVxRuHsJdGfOiAy2MnE?mode=view

Looking forward to heard back from you,

Designs look the same

We need a WordPress ecommerce website theme/template for a new company named Pavreno (a play on words for BERUNDA the inventor of Vextrum). Pavreno will provide metaverse services such as: • Pavreno Coin • Pavreno wallet • Pavreno Exchange • Pavreno NFT • Pavreno Tech • Pavreno Pay • Pavreno CaaS (community as a service) • Pavreno CRM • Pavreno Experience • Pavreno Blockchain • Pavreno Commerce • Pavreno Space (as in outer space) • Pavreno Art (sub of NFT) • Pavreno Store You can find our actual logo at the following link, in order to show us templates aligned with our brand: https://files.plomvarek.com/share/folders/7kWmTzeQaLpYbNcVxRuHsJdGfOiAy2MnE?mode=view Looking forward to heard back from you,

Target Market(s)

Blockchain & Cryptocurrency Businesses

Industry/Entity Type

B2C, B2B Services.

Font styles to use
Other font styles liked:
• Monserrat, Helvetica, Object Sans

Requirements
Nice to have
• Light background picture,
Should not have
• Arch designs

```html
<!DOCTYPE html>
<html lang="en">
<head>
<meta charset="utf-8">
<title>Pavreno — Education, certifications, crypto experts and investors</title>
<link href="https://fonts.googleapis.com/css2?family=Montserrat:wght@300;400;500;600;700;800&family=Roboto:wght@400;500&display=swap" rel="stylesheet">
<style>
:root{
  --bg:#121420;
  --panel:#1d1f2c;
  --panel-2:#222534;
  --cyan:#27c6e6;
  --blue:#2f6fe4;
  --bar-top:#3b55d6;
  --white:#ffffff;
  --muted:#b7bac6;
  --dim:#7c8092;
  --red:#e24a4a;
  --green:#3ccf7a;
  --heading:"Montserrat",sans-serif;
  --body:"Roboto",sans-serif;
}
*{margin:0;padding:0;box-sizing:border-box}
html,body{width:1200px;height:3873px;overflow:hidden;background:var(--bg)}
body{font-family:var(--body);color:var(--white)}
.page{position:relative;width:1200px;height:3873px;overflow:hidden;background:var(--bg)}
.abs{position:absolute}
.brand{font-family:var(--heading);font-weight:600;font-size:34px;letter-spacing:.5px;display:flex;align-items:center;gap:12px;color:var(--white)}
.brand-mark{width:30px;height:30px;border:3px solid var(--white);display:inline-block}
.nav{top:34px;left:413px;display:flex;font-family:var(--heading);font-weight:600;font-size:14.5px}
.nav a{color:var(--white);text-decoration:none;margin-right:22px}
.lang{top:34px;left:1012px;font-size:14px;display:flex;align-items:center;gap:8px;color:var(--white)}
.lang i{width:17px;height:17px;border-radius:50%;background:linear-gradient(#e23b3b 50%,#2f55c9 50%);display:inline-block}
.eyebrow{font-family:var(--heading);font-weight:500;color:var(--cyan);font-size:18px;letter-spacing:.3px}
.hero-title{top:232px;left:97px;font-family:var(--heading);font-weight:300;font-size:41px;line-height:51px;white-space:nowrap}
.hero-title b{font-weight:700}
.hero-text{top:398px;left:100px;width:430px;font-size:14.5px;line-height:26px;color:#e6e8ee}
.btn{display:inline-flex;align-items:center;justify-content:center;gap:10px;border-radius:24px;background:linear-gradient(90deg,#2aa8e6,#1f7fd8);font-family:var(--heading);font-weight:700;font-size:14px;color:var(--white);text-transform:uppercase}
.btn .arrow{width:14px;height:14px;border-radius:50%;background:var(--white);position:relative}
.btn .arrow:after{content:"";position:absolute;left:4px;top:4px;border-left:6px solid #1f7fd8;border-top:3px solid transparent;border-bottom:3px solid transparent}
.socials{display:flex;gap:20px}
.socials span{width:14px;height:14px;border-radius:3px;background:var(--white);display:block}
.hero-art{top:80px;left:580px;width:580px;height:480px;border-radius:8px;background:radial-gradient(ellipse at 55% 45%,#1fb6ea 0%,#1a6fd0 35%,rgba(18,20,32,0) 70%)}
.ticker{top:668px;left:98px;width:1010px;display:flex}
.coin{width:262px;display:flex;gap:10px}
.coin-dot{width:36px;height:36px;border-radius:50%;flex:none;margin-top:4px}
.coin-name{font-family:var(--heading);font-weight:600;font-size:15px}
.coin-name small{font-size:9px;font-weight:500;margin-left:5px}
.coin-sub{font-size:10px;color:#d5d7de;display:flex;justify-content:space-between;width:165px;margin-top:2px}
.coin-cap{font-size:15px;font-weight:500;margin-top:5px}
.token{top:782px;left:100px;width:1000px;height:280px;background:var(--panel)}
.count{top:45px;left:38px;display:flex;align-items:flex-start;gap:12px}
.unit{text-align:center}
.unit b{display:block;font-family:var(--heading);font-weight:500;font-size:36px;line-height:40px}
.unit span{font-size:11px;color:var(--dim)}
.sep{color:var(--blue);font-size:28px;line-height:40px}
.bar{position:absolute;bottom:0;width:50px;background:linear-gradient(var(--bar-top),rgba(40,55,140,.15))}
.bar-label{position:absolute;font-family:var(--heading);font-weight:600;font-size:15px;width:60px;text-align:center}
.token-title{top:95px;left:765px;font-family:var(--heading);font-size:31px;line-height:38px}
.token-title span{color:var(--cyan);font-weight:400;display:block}
.token-title b{font-weight:700}
.about-art{top:1130px;left:220px;width:360px;height:380px;background:radial-gradient(circle at 55% 40%,#1d8fd8 0%,#124a8a 40%,rgba(18,20,32,0) 72%)}
.about-text{top:1160px;left:650px;width:450px}
.about-text h2{font-family:var(--heading);font-weight:400;font-size:42px;margin-top:6px;letter-spacing:.5px}
.about-text h2 b{font-weight:700}
.about-text p{font-size:14px;line-height:26px;color:#e2e4ea;margin-top:14px}
.feature{top:1555px;width:237px;height:250px;background:var(--panel-2);text-align:center;padding-top:38px}
.feature.active{box-shadow:inset 0 0 0 2px var(--blue);background:#1b1e2c}
.feature svg{width:76px;height:76px}
.feature h3{font-family:var(--heading);font-weight:600;font-size:17px;margin-top:12px}
.feature p{font-size:12.5px;line-height:22px;color:var(--muted);margin:8px 14px 0}
.section-head{left:0;width:1200px;text-align:center}
.section-head .eyebrow{font-size:18px}
.section-head h2{font-family:var(--heading);font-weight:400;font-size:44px;margin-top:8px}
.section-head h2 b{font-weight:700}
.road-line{top:2134px;left:0;width:1200px;height:2px;background:var(--cyan)}
.node{width:26px;height:26px;border-radius:50%;border:2px solid var(--cyan);background:var(--bg)}
.node:after{content:"";position:absolute;left:6px;top:6px;width:10px;height:10px;border-radius:50%;background:var(--cyan)}
.stem{width:2px;height:24px;background:var(--cyan)}
.stem:after{content:"";position:absolute;left:-2px;width:6px;height:6px;border-radius:50%;background:var(--cyan)}
.stem.up:after{top:-4px}.stem.down:after{bottom:-4px}
.milestone{width:200px;text-align:center}
.milestone small{display:block;font-size:11px;color:var(--muted);letter-spacing:.3px}
.milestone b{display:block;font-family:var(--heading);font-weight:700;font-size:17px;margin-top:3px}
.course{top:2442px;width:318px;height:400px;background:var(--panel-2);text-align:center}
.course .photo{height:218px}
.course h3{font-family:var(--heading);font-weight:600;font-size:22px;margin-top:22px}
.course p{font-size:14px;line-height:26px;color:#e2e4ea;margin:8px 14px 0}
.course a{display:inline-block;margin-top:8px;font-family:var(--heading);font-weight:600;font-size:12.5px;color:var(--cyan);text-decoration:underline}
.member{top:3060px;width:237px;height:312px}
.member .photo{position:absolute;inset:0;background:linear-gradient(160deg,#5a5a5a,#1e1e1e)}
.member .name{position:absolute;bottom:0;left:0;width:217px;height:42px;background:#252730;font-family:var(--heading);font-weight:600;font-size:17px;display:flex;align-items:center;justify-content:center}
.foot-social{top:3643px;left:124px;display:flex;gap:15px}
.foot-social span{width:34px;height:34px;border-radius:50%;background:#2a2d3a;display:block}
.foot-col h4{font-family:var(--heading);font-weight:700;font-size:17px;text-transform:uppercase}
.foot-col ul{list-style:none;margin-top:12px}
.foot-col li{font-size:15px;line-height:32px}
.contact-row{display:flex;gap:12px;align-items:flex-start;margin-top:12px;font-size:15px;line-height:21px}
.contact-row i{width:38px;height:38px;border-radius:50%;background:var(--blue);flex:none;display:flex;align-items:center;justify-content:center}
.subscribe{margin-top:16px;width:245px;height:42px;border-radius:21px;background:var(--white);position:relative;color:#555;font-size:14px;padding:12px 0 0 20px}
.subscribe i{position:absolute;right:0;top:0;width:50px;height:42px;border-radius:21px;background:linear-gradient(90deg,#2aa8e6,#1f7fd8);display:flex;align-items:center;justify-content:center}
.foot-rule{top:3815px;left:100px;width:1000px;height:1px;background:#2a2d3a}
.copyright{top:3840px;left:0;width:1200px;text-align:center;font-size:14px}
</style>
</head>
<body>
<div class="page">

  <header>
    <div class="abs brand" style="top:22px;left:100px"><span class="brand-mark"></span>PAVRENO</div>
    <nav class="abs nav">
      <a href="#">About Us</a><a href="#">Services</a><a href="#">Cryptocurrency Certifications</a><a href="#">Faq’s</a><a href="#">Contact Us</a>
    </nav>
    <div class="abs lang"><i></i>English ⌄</div>
  </header>

  <section class="hero">
    <div class="abs eyebrow" style="top:207px;left:100px">WELCOME TO PAVRENO</div>
    <h1 class="abs hero-title">Education, certifications,<br>Crypto-<b>Experts and</b><br><b>Investors.</b></h1>
    <p class="abs hero-text">Lorem ipsum dolor sit amet, consectetur adipiscing elit, sed do eiusmod tempor incididunt ut labore</p>
    <a class="abs btn" style="top:471px;left:100px;width:178px;height:46px">Get Started <span class="arrow"></span></a>
    <div class="abs socials" style="top:487px;left:296px"><span></span><span></span><span></span><span></span></div>
    <div class="abs hero-art" role="img" aria-label="Isometric illustration of blockchain server platforms and a glowing coin"></div>
  </section>

  <section class="abs ticker">
    <div class="coin"><span class="coin-dot" style="background:#f39a1e"></span><div><div class="coin-name">Vextrum <small style="color:var(--red)">-11.35</small></div><div class="coin-sub"><span>$6,675.00</span><span style="color:var(--red)">-0.17%</span></div><div class="coin-cap">$115,923,000,947.000</div></div></div>
    <div class="coin"><span class="coin-dot" style="background:#2d3044"></span><div><div class="coin-name">Aetheron <small style="color:var(--green)">2.00</small></div><div class="coin-sub"><span>$241.31</span><span style="color:var(--green)">0.96</span></div><div class="coin-cap">$24,718,133,018.00</div></div></div>
    <div class="coin"><span class="coin-dot" style="background:#27b36b"></span><div><div class="coin-name">Corvane Cash <small style="color:var(--green)">0.92</small></div><div class="coin-sub"><span>$1483.87</span><span style="color:var(--green)">$483.87</span></div><div class="coin-cap">$8,425,785,462.00</div></div></div>
    <div class="coin"><span class="coin-dot" style="background:#f0b33a"></span><div><div class="coin-name">Zelvix <small style="color:var(--green)">2.00</small></div><div class="coin-sub"><span>$131.97</span><span style="color:var(--green)">1.52%</span></div><div class="coin-cap">$640,769,378.00</div></div></div>
  </section>

  <section class="abs token">
    <div class="abs count">
      <div class="unit"><b>12</b><span>Days</span></div><div class="sep">:</div>
      <div class="unit"><b>04</b><span>Hours</span></div><div class="sep">:</div>
      <div class="unit"><b>02</b><span>Minutes</span></div><div class="sep">:</div>
      <div class="unit"><b>12</b><span>Seconds</span></div>
    </div>
    <div class="abs" style="top:152px;left:152px;font-size:11px;color:var(--cyan)">200.000.PVR</div>
    <div class="abs" style="top:152px;left:282px;font-size:11px;font-weight:500">500.000.000 PVR</div>
    <div class="abs" style="top:171px;left:55px;width:330px;height:3px;background:#d6d8de"></div>
    <div class="abs" style="top:171px;left:55px;width:188px;height:3px;background:var(--cyan)"></div>
    <div class="abs" style="top:164px;left:234px;width:17px;height:17px;border-radius:50%;border:2px solid var(--cyan);background:var(--panel)"></div>
    <div class="abs" style="top:186px;left:268px;font-size:10px;color:var(--dim)">PVR RAISED: 500.000</div>

    <div class="bar" style="left:468px;height:210px"></div>
    <div class="bar" style="left:536px;height:107px"></div>
    <div class="bar" style="left:603px;height:144px"></div>
    <div class="bar" style="left:671px;height:187px"></div>
    <div class="bar-label" style="left:463px;top:44px">40%</div>
    <div class="bar-label" style="left:531px;top:149px">10%</div>
    <div class="bar-label" style="left:598px;top:112px">20%</div>
    <div class="bar-label" style="left:666px;top:68px">30%</div>

    <h2 class="abs token-title"><span>TOKEN SALE</span><b>ALLOCATION</b></h2>
    <a class="abs btn" style="top:193px;left:763px;width:178px;height:46px">Buy Token <span class="arrow"></span></a>
  </section>

  <section class="about">
    <div class="abs about-art" role="img" aria-label="Network mesh shield illustration with a gold coin"></div>
    <div class="abs about-text">
      <div class="eyebrow">ABOUT US</div>
      <h2>PAV<b>RENO</b></h2>
      <p>Lorem ipsum dolor sit amet, consectetur adipiscing elit, d do eiusmod tempor incididunt ut labore Lorem ipsu sit amet, consectur adipiscing elit, sed do eiusmod tempor incididunt ut laboreLorem ipsum dolor sit amet, consectetur adipiscing elit,</p>
      <p>Sed ut perspics iste natus error sit voluptatem usantium doloremque laudantium, totam rem aperiipsa quae ab illo inveore veritatis et quasi architecto beatae vitae dicta sunt exabo. Nemo em ipsam voluptatem quia voluptas sit aspernatur aut odit aut fugi</p>
    </div>
  </section>

  <section class="features">
    <article class="abs feature" style="left:100px">
      <svg viewBox="0 0 76 76" fill="none" stroke="var(--blue)" stroke-width="2.5"><circle cx="38" cy="38" r="33"/><circle cx="38" cy="38" r="24"/></svg>
      <h3>Finibus Bonorum</h3><p>Lorem ipsum dolor amet, consectetur adipiscing elit, sed do</p>
    </article>
    <article class="abs feature active" style="left:354px">
      <svg viewBox="0 0 76 76" fill="none" stroke="var(--blue)" stroke-width="2.5"><rect x="27" y="8" width="22" height="20"/><rect x="8" y="30" width="22" height="20"/><rect x="46" y="30" width="22" height="20"/><rect x="27" y="50" width="22" height="20"/></svg>
      <h3>Finibus Bonorum</h3><p>Lorem ipsum dolor amet, consectetur adipiscing elit, sed do</p>
    </article>
    <article class="abs feature" style="left:607px">
      <svg viewBox="0 0 76 76" fill="none" stroke="var(--blue)" stroke-width="2.5"><circle cx="38" cy="38" r="28"/><circle cx="38" cy="38" r="12"/><path d="M6 6l18 18M70 6L52 24M6 70l18-18M70 70L52 52"/></svg>
      <h3>Finibus Bonorum</h3><p>Lorem ipsum dolor amet, consectetur adipiscing elit, sed do</p>
    </article>
    <article class="abs feature" style="left:861px">
      <svg viewBox="0 0 76 76" fill="none" stroke="var(--blue)" stroke-width="2.5"><circle cx="38" cy="26" r="14"/><path d="M8 70h60M14 70V54M24 70V48M52 70V48M62 70V40"/></svg>
      <h3>Finibus Bonorum</h3><p>Lorem ipsum dolor amet, consectetur adipiscing elit, sed do</p>
    </article>
  </section>

  <section class="roadmap">
    <div class="abs section-head" style="top:1902px"><div class="eyebrow">ROADMAP</div><h2>How It <b>All Started</b></h2></div>
    <div class="abs road-line"></div>

    <div class="abs node" style="top:2122px;left:156px"></div>
    <div class="abs node" style="top:2122px;left:329px"></div>
    <div class="abs node" style="top:2122px;left:502px"></div>
    <div class="abs node" style="top:2122px;left:675px"></div>
    <div class="abs node" style="top:2122px;left:847px"></div>
    <div class="abs node" style="top:2122px;left:1020px"></div>

    <div class="abs stem up" style="top:2094px;left:342px"></div>
    <div class="abs stem up" style="top:2094px;left:688px"></div>
    <div class="abs stem up" style="top:2094px;left:1033px"></div>
    <div class="abs stem down" style="top:2150px;left:169px"></div>
    <div class="abs stem down" style="top:2150px;left:515px"></div>
    <div class="abs stem down" style="top:2150px;left:860px"></div>

    <div class="abs milestone" style="top:2033px;left:242px"><small>FINIBUS BONORUM ET</small><b>February 2021</b></div>
    <div class="abs milestone" style="top:2033px;left:588px"><small>FINIBUS BONORUM ET</small><b>February 2021</b></div>
    <div class="abs milestone" style="top:2033px;left:933px"><small>FINIBUS BONORUM ET</small><b>June 2021</b></div>
    <div class="abs milestone" style="top:2196px;left:69px"><small>FINIBUS BONORUM ET</small><b>January 2021</b></div>
    <div class="abs milestone" style="top:2196px;left:415px"><small>FINIBUS BONORUM ET</small><b>March2021</b></div>
    <div class="abs milestone" style="top:2196px;left:760px"><small>FINIBUS BONORUM ET</small><b>May2021</b></div>
  </section>

  <section class="education">
    <div class="abs section-head" style="top:2330px"><div class="eyebrow">CLASS</div><h2>Our <b>Education</b></h2></div>
    <article class="abs course" style="left:100px">
      <div class="photo" role="img" aria-label="Photo of hands typing on a keyboard with market charts" style="background:linear-gradient(135deg,#c9d4dc,#6f8ea6 60%,#1e3e66)"></div>
      <h3>Finibus Bonorum</h3><p>Lorem ipsum dolor sit amet, cotur adipiscing elit, sed do eiusmod tempor ididunt ut labore et dolore magna aliqua.</p><a href="#">LEARN MORE</a>
    </article>
    <article class="abs course" style="left:440px">
      <div class="photo" role="img" aria-label="Photo of a person working on a laptop" style="background:linear-gradient(135deg,#e3e0da,#8d8a86 55%,#3d4250)"></div>
      <h3>Finibus Bonorum</h3><p>Lorem ipsum dolor sit amet, cotur adipiscing elit, sed do eiusmod tempor ididunt ut labore et dolore magna aliqua.</p><a href="#">LEARN MORE</a>
    </article>
    <article class="abs course" style="left:781px">
      <div class="photo" role="img" aria-label="Photo of a trader with a tablet over trading charts" style="background:linear-gradient(135deg,#2b6bc4,#1a3f7e 55%,#0e1f44)"></div>
      <h3>Finibus Bonorum</h3><p>Lorem ipsum dolor sit amet, cotur adipiscing elit, sed do eiusmod tempor ididunt ut labore et dolore magna aliqua.</p><a href="#">LEARN MORE</a>
    </article>
  </section>

  <section class="team">
    <div class="abs section-head" style="top:2938px"><div class="eyebrow">MEET OUR BRILLIANT MINDS</div><h2>Our <b>Motivated Team</b></h2></div>
    <article class="abs member" style="left:100px"><div class="photo" role="img" aria-label="Black and white portrait of a team member"></div><div class="name">Dorian Hale</div></article>
    <article class="abs member" style="left:354px"><div class="photo" role="img" aria-label="Black and white portrait of a team member"></div><div class="name">Dorian Hale</div></article>
    <article class="abs member" style="left:607px"><div class="photo" role="img" aria-label="Black and white portrait of a team member" style="background:linear-gradient(160deg,#2a2a2a,#111)"></div><div class="name">Dorian Hale</div></article>
    <article class="abs member" style="left:861px"><div class="photo" role="img" aria-label="Black and white portrait of a team member"></div><div class="name">Dorian Hale</div></article>
  </section>

  <footer>
    <div class="abs brand" style="top:3566px;left:100px"><span class="brand-mark"></span>PAVRENO</div>
    <div class="abs foot-social"><span></span><span></span><span></span><span></span></div>
    <div class="abs foot-col" style="top:3570px;left:355px">
      <h4>Quick Links</h4>
      <ul><li>About Us</li><li>Services</li><li>Cryptocurrency Certifications</li><li>Faq’s</li><li>Contact Us</li></ul>
    </div>
    <div class="abs foot-col" style="top:3570px;left:580px">
      <h4>Contact Us</h4>
      <div class="contact-row"><i><svg width="14" height="18" viewBox="0 0 14 18"><path d="M7 0a7 7 0 0 0-7 7c0 5 7 11 7 11s7-6 7-11a7 7 0 0 0-7-7z" fill="#fff"/><circle cx="7" cy="7" r="2.5" fill="var(--blue)"/></svg></i><span>4820 Larkmoor Avenue<br>Brellton 30418</span></div>
      <div class="contact-row"><i><svg width="16" height="16" viewBox="0 0 16 16"><path d="M3 1l3 3-2 2c1 2 3 4 6 6l2-2 3 3-2 2C7 15 1 9 1 3z" fill="#fff"/></svg></i><span style="padding-top:8px">123-555-0147</span></div>
      <div class="contact-row"><i><svg width="18" height="13" viewBox="0 0 18 13"><rect width="18" height="13" rx="1" fill="#fff"/><path d="M1 1l8 6 8-6" stroke="var(--blue)" fill="none" stroke-width="1.5"/></svg></i><span style="padding-top:8px">info@pavreno.com</span></div>
    </div>
    <div class="abs foot-col" style="top:3570px;left:860px;width:245px">
      <h4>Keep Updated</h4>
      <p style="font-size:15px;line-height:24px;margin-top:10px">Lorem ipsum dolor set adipiscing elit, sed do eiusmod tempor</p>
      <div class="subscribe">Your Email<i><svg width="18" height="16" viewBox="0 0 18 16"><path d="M0 7L18 0l-4 16-5-5-3 3V10l9-8-11 6z" fill="#fff"/></svg></i></div>
    </div>
    <div class="abs foot-rule"></div>
    <p class="abs copyright">Copyright © 2021PAVRENO All rights reserved.</p>
  </footer>

</div>
</body>
</html>
```